I need a folder to put papers in when I am scheduling patients for surgery. The information is general, such as costs, consent forms etc. The folder is designed to give the patient these papers in a neat manner. The cover of the folder needs to use my brand and perhaps create some interest when it is sitting on their kitchen bench with visitors and family. I'll attach a typical template for a folder. It needs to be stylish, classic and professional, as I am about to operate on the person's eye. <br/>I would like my logo included. I'll also attach a photo which is on my website which might work to wrap around the folder. The website address is bramwelkoske.com.au and you can see the way the image is used there on most of the pages as a banner. My profile photo could possibly used as well. Perhaps on the back, but if it looks strange then that is not necessary. The contact information need not be on the folder. Just Dr Lars Brimwell, Ophthalmic Surgeon. Finally, our brand slogan is. "The world's a beautiful place, see it clearly". This could also be on it. Again, this all needs to be professional looking. <br/>I've attached all our previous design jobs, 2 profile pictures, and the image that I think would work. Please also look at the website. <br/><br/>The second part of the project is to create a business card for my practice manager. Her name is Fiona Pelkrest<br/>It should include<br/>Fiona Pelkrest (BCom)<br/>Practice Manager for Dr Lars Brimwell<br/>Ophthalmic Surgeon <br/><br/>Then all the details which are on our current business card<br/><br/><br/><br/><br/>

Contact Information for Business Card

Just match the business cards I already have, but use the details above

Colors

Designer to choose colors to be used in the design.

```html
<!DOCTYPE html>
<html lang="en">
<head>
<meta charset="utf-8">
<title>Dr Lars Brimwell – Patient Folder</title>
<link rel="stylesheet" href="https://fonts.googleapis.com/css2?family=Open+Sans:wght@400;600;700&display=swap">
<style>
  :root {
    --canvas: #d9d9d9;
    --paper: #f1f1f1;
    --paper-light: #f4f4f4;
    --brand-deep: #1d4fb0;
    --brand-mid: #2f6cc4;
    --brand-light: #4a9fd6;
    --text-dark: #3a3a3a;
  }
  * { margin: 0; padding: 0; box-sizing: border-box; }
  html, body {
    width: 1200px;
    height: 900px;
    overflow: hidden;
    background: var(--canvas);
    font-family: "Open Sans", Arial, sans-serif;
  }
  .folder {
    position: absolute;
    left: 170px;
    top: 150px;
    width: 860px;
    height: 600px;
    display: flex;
    box-shadow: 0 18px 40px rgba(0,0,0,0.18);
  }
  .panel {
    position: relative;
    width: 430px;
    height: 600px;
    overflow: hidden;
    background: var(--paper);
  }
  .band {
    position: absolute;
    left: 0;
    width: 100%;
    height: 58px;
    background: radial-gradient(ellipse at 55% 50%, var(--brand-light) 0%, var(--brand-mid) 35%, var(--brand-deep) 100%);
  }
  .band--top { top: 0; }
  .band--bottom { bottom: 0; }

  .brand {
    position: absolute;
    display: flex;
    align-items: center;
    gap: 10px;
  }
  .brand__dot {
    width: 32px;
    height: 32px;
    border-radius: 50%;
    background: var(--brand-mid);
    flex: none;
  }
  .brand__name {
    font-weight: 600;
    font-size: 21px;
    line-height: 1;
    color: var(--brand-mid);
    white-space: nowrap;
  }
  .brand__role {
    font-weight: 700;
    font-size: 8px;
    color: var(--text-dark);
    margin-top: 4px;
  }
  .brand__creds {
    font-weight: 400;
    font-size: 6.5px;
    color: var(--text-dark);
  }
  .back .brand { left: 88px; top: 250px; }
  .front .brand { left: 196px; top: 522px; }

  .front-art { position: absolute; inset: 0; width: 100%; height: 100%; }
  .fold-line {
    position: absolute;
    left: 430px; top: 0;
    width: 1px; height: 600px;
    background: rgba(0,0,0,0.08);
  }
</style>
</head>
<body>
  <main class="folder">
    <section class="panel back">
      <div class="band band--top"></div>
      <div class="brand">
        <span class="brand__dot"></span>
        <div class="brand__text">
          <div class="brand__name">Dr Lars Brimwell</div>
          <div class="brand__role">Ophthalmic Surgeon</div>
          <div class="brand__creds">MBBS (Hons) MMed FRANZCO</div>
        </div>
      </div>
      <div class="band band--bottom"></div>
    </section>

    <section class="panel front">
      <svg class="front-art" viewBox="0 0 430 600">
        <defs>
          <radialGradient id="brandGlow" gradientUnits="userSpaceOnUse" cx="170" cy="470" r="430">
            <stop offset="0" stop-color="#4a9fd6"/>
            <stop offset="0.35" stop-color="#2f6cc4"/>
            <stop offset="1" stop-color="#1d4fb0"/>
          </radialGradient>
          <linearGradient id="photoTone" x1="0" y1="0" x2="0" y2="1">
            <stop offset="0" stop-color="#e4e6e8"/>
            <stop offset="0.45" stop-color="#b8b2aa"/>
            <stop offset="1" stop-color="#b88a5e"/>
          </linearGradient>
        </defs>
        <rect width="430" height="600" fill="url(#brandGlow)"/>
        <circle cx="205" cy="235" r="205" fill="url(#photoTone)" role="img" aria-label="Photograph: a team gathered around a table with laptops in a bright room"/>
        <path class="wave-blue" d="M0 300 C 70 295, 120 330, 160 385 C 195 430, 240 450, 290 440 L 430 420 L 430 600 L 0 600 Z" fill="url(#brandGlow)"/>
        <path class="wave-white" d="M150 600 C 160 510, 230 458, 320 448 C 390 440, 420 400, 430 330 L 430 600 Z" fill="#f4f4f4"/>
      </svg>
      <div class="brand">
        <span class="brand__dot"></span>
        <div class="brand__text">
          <div class="brand__name">Dr Lars Brimwell</div>
          <div class="brand__role">Ophthalmic Surgeon</div>
          <div class="brand__creds">MBBS (Hons) MMed FRANZCO</div>
        </div>
      </div>
    </section>
    <div class="fold-line"></div>
  </main>
</body>
</html>
```